Wordpress Design Project

We are a local restaurant who needs a quality online identity base. We operate in a 1930's Villa, and our target market is the below mid - upper. Our main sale is the evening dinner meal, while we also sell home-made goods, including preserves, and handmade chocolates.
The final Wordpress coded design will:
Be a base for information including Contact details, and a Map of it's location. It will also include photographs of some of the dishes to give an idea to potential customers as to the style and target market.
The site will have 4 main pages
-Main
-About
-Menu
-Contact
Ideas for elements we would like to have included in the design are
Cardboard tags with the links to the other pages, which give a home-made feel
Character wood, with deep grain to emphasis our homely feel
An 'aged' map of the location. Possibly on a large cardboard tag.
Link to our Friendbook page
Link to our Plate Finder review page http://www.platefinder.co.nz/restaurant.php?rest=4273
Notes:
The final Wordpress site should communicate a homely inviting image, with deep character, while still looking elegant and slightly simplistic. We would like fine fonts, with nice spacing, especially on the cardboard tags.
I have attached a mockup of our very loose vision for the site to give you an idea of the line we would like to go down. This is just for initial ideas, and we are happy for radically different designs, or just neat variations on the base design
Professional, edited photos of the food available will be uploaded alongside this project
Villa Rosmar does not have an official Logo for use on the website, so a simple header that ties in with the page will be fine. This may be replaced eventually with a new logo
Address and Hosting is already setup with the address being www.villarosmarresturant.co.nz with a placeholder site online.
We look forward to all designs, and welcome any questions. This should be an nice job for someone with an eye for detail.

```html
<!DOCTYPE html>
<html lang="en">
<head>
<meta charset="utf-8">
<title>Villa Rosmar – The Restaurant</title>
<link rel="stylesheet" href="https://fonts.googleapis.com/css2?family=Arimo:wght@400&family=Open+Sans:wght@600;700&family=Questrial&display=swap">
<style>
  :root {
    --wood-dark: #2a130a;
    --wood-mid: #6b3418;
    --wood-light: #8a4a24;
    --plaque-light: #ecd7ad;
    --plaque-dark: #c9a878;
    --ink-brown: #2b170a;
    --tag-dark: #2c2c2c;
    --tag-text: #9a9a9a;
    --tag-active: #f3dcb0;
    --page-dark: #141414;
    --page-rim: #7d6044;
    --gold: #e9c98a;
    --text-light: #d4d4d4;
    --text-muted: #bdbdbd;
    --footer-text: #e6d2b4;
    --button-gold: #c9a45c;
  }
  html, body {
    margin: 0;
    padding: 0;
    overflow: hidden;
  }
  .canvas {
    position: relative;
    width: 1200px;
    height: 1139px;
    overflow: hidden;
    background:
      repeating-linear-gradient(180deg, rgba(0,0,0,0) 0 118px, rgba(20,6,2,.55) 118px 124px, rgba(0,0,0,0) 124px 130px),
      radial-gradient(ellipse at 50% 35%, var(--wood-light) 0%, var(--wood-mid) 45%, var(--wood-dark) 100%);
    font-family: "Arimo", Arial, sans-serif;
  }
  .location-tag {
    position: absolute;
    left: 943px; top: 10px;
    width: 181px; height: 53px;
    box-sizing: border-box;
    background: linear-gradient(180deg, #f0d49a, #c99a55);
    border: 4px solid #4a2612;
    border-radius: 3px;
    display: flex; align-items: center; gap: 14px;
    padding-left: 20px;
    font-family: "Questrial", sans-serif;
    font-size: 17px;
    color: var(--ink-brown);
  }
  .location-tag .pin-box {
    width: 34px; height: 34px;
    background: #f6ecd6;
    border: 1px solid #8a6a40;
    border-radius: 3px;
  }
  .site-header {
    position: absolute;
    left: 332px; top: 38px;
    width: 539px; height: 180px;
  }
  .site-header svg { position: absolute; inset: 0; }
  .brand {
    position: absolute; inset: 0;
    display: flex; flex-direction: column; align-items: center; justify-content: center;
  }
  .brand-name {
    font-family: "Questrial", sans-serif;
    font-size: 60px;
    color: var(--ink-brown);
    letter-spacing: 2px;
    margin-top: -6px;
  }
  .brand-tagline {
    align-self: flex-end;
    margin-right: 74px;
    font-family: "Questrial", sans-serif;
    font-size: 15px;
    color: var(--ink-brown);
    letter-spacing: 1px;
  }
  .strings { position: absolute; left: 0; top: 0; }
  .main-nav {
    position: absolute;
    top: 304px; left: 289px;
    display: flex; gap: 10px;
  }
  .nav-tag {
    width: 145px; height: 42px;
    background: linear-gradient(180deg, #3a3a3a, var(--tag-dark));
    border: 1px solid #111;
    box-shadow: 0 6px 10px rgba(0,0,0,.5);
    display: flex; align-items: center; justify-content: center;
    font-family: "Open Sans", sans-serif;
    font-weight: 700;
    font-size: 22px;
    color: var(--tag-text);
    text-decoration: none;
    letter-spacing: .5px;
  }
  .nav-tag.is-active { color: var(--tag-active); }
  .book { position: absolute; left: 0; top: 0; }
  .hero-photo-label { position: absolute; }
  .page-content {
    position: absolute;
    left: 672px; top: 455px;
    width: 438px;
  }
  .section-title {
    font-family: "Questrial", sans-serif;
    font-size: 23px;
    color: var(--text-light);
    margin: 0;
  }
  .section-title .accent { color: var(--gold); }
  .title-rule {
    width: 365px; height: 6px; margin: 6px 0 14px -2px;
    background: repeating-linear-gradient(135deg, #8a8a8a 0 1px, transparent 1px 4px);
    opacity: .7;
  }
  .intro-text {
    margin: 0;
    font-size: 15px;
    line-height: 26.5px;
    color: var(--text-light);
    text-align: justify;
  }
  .category-title {
    font-family: "Questrial", sans-serif;
    font-size: 24px;
    color: var(--gold);
    margin: 16px 0 0;
  }
  .category-item {
    position: absolute; left: 704px; top: 786px;
  }
  .item-photo {
    position: absolute; left: 0; top: 14px;
    width: 123px; height: 128px;
    box-sizing: border-box;
    border: 3px solid #555;
    border-radius: 8px;
    background: radial-gradient(circle at 50% 55%, #e8d2b0 0%, #7a3a1c 45%, #3a1208 100%);
  }
  .item-title {
    position: absolute; left: 148px; top: 0;
    width: 270px;
    margin: 0; padding-bottom: 6px;
    border-bottom: 1px solid #333;
    font-family: "Questrial", sans-serif;
    font-size: 23px;
    color: var(--text-light);
  }
  .item-text {
    position: absolute; left: 148px; top: 37px;
    width: 218px;
    margin: 0;
    font-size: 14px;
    line-height: 19px;
    color: var(--text-muted);
    text-align: justify;
  }
  .item-more {
    position: absolute; left: 148px; top: 102px;
    margin: 0;
    font-size: 14px;
    color: var(--text-muted);
  }
  .site-footer .footer-links {
    position: absolute; top: 1033px; left: 400px;
    display: flex; gap: 18px;
    font-size: 14px; color: var(--footer-text);
  }
  .footer-links a { color: inherit; text-decoration: none; }
  .footer-links .sep { opacity: .8; }
  .copyright {
    position: absolute; top: 1065px; left: 0; width: 1200px;
    text-align: center; padding-left: 0;
    font-size: 14px; color: var(--footer-text);
    margin: 0;
    text-indent: 0;
  }
  .copyright span { position: relative; left: 0; }
  .social-link {
    position: absolute; left: 875px; top: 1023px;
    display: flex; gap: 4px; text-decoration: none;
  }
  .social-link .visit {
    width: 185px; height: 43px;
    background: linear-gradient(180deg, #e3c47c, var(--button-gold));
    border-radius: 3px;
    display: flex; align-items: center; justify-content: center;
    font-family: "Open Sans", sans-serif; font-weight: 700;
    font-size: 20px; color: #3a2410; letter-spacing: 1px;
  }
  .social-link .network {
    height: 43px; padding: 0 10px;
    background: linear-gradient(180deg, #e3c47c, var(--button-gold));
    border-radius: 3px;
    display: flex; align-items: center;
    font-family: "Open Sans", sans-serif; font-weight: 700;
    font-size: 16px; color: #3a2410;
  }
</style>
</head>
<body>
<div class="canvas">

  <a class="location-tag" href="#location"><span class="pin-box"></span>Location</a>

  <header class="site-header">
    <svg width="539" height="180" viewBox="0 0 539 180">
      <defs>
        <linearGradient id="plaqueFill" x1="0" y1="0" x2="1" y2="1">
          <stop offset="0" stop-color="#f2e0bb"/>
          <stop offset=".5" stop-color="var(--plaque-light)"/>
          <stop offset="1" stop-color="var(--plaque-dark)"/>
        </linearGradient>
      </defs>
      <path d="M60 8 H479 Q485 30 505 32 Q535 60 535 90 Q535 120 505 148 Q485 150 479 172 H60 Q54 150 34 148 Q4 120 4 90 Q4 60 34 32 Q54 30 60 8 Z" fill="url(#plaqueFill)" stroke="#a88456" stroke-width="2"/>
      <circle cx="55" cy="90" r="10" fill="#6a6a6a"/>
      <circle cx="484" cy="90" r="10" fill="#6a6a6a"/>
    </svg>
    <div class="brand">
      <span class="brand-name">Villa Rosmar</span>
      <span class="brand-tagline">THE RESTAURANT</span>
    </div>
  </header>

  <svg class="strings" width="1200" height="310" viewBox="0 0 1200 310">
    <g stroke="#222" stroke-width="2" fill="none">
      <path d="M299 306 L362 254 L424 306"/>
      <path d="M455 306 L518 254 L580 306"/>
      <path d="M611 306 L674 254 L736 306"/>
      <path d="M767 306 L830 254 L892 306"/>
    </g>
    <g fill="#9a9a9a">
      <circle cx="362" cy="254" r="5"/><circle cx="518" cy="254" r="5"/>
      <circle cx="674" cy="254" r="5"/><circle cx="830" cy="254" r="5"/>
    </g>
  </svg>

  <nav class="main-nav">
    <a class="nav-tag is-active" href="#home">HOME</a>
    <a class="nav-tag" href="#about">ABOUT US</a>
    <a class="nav-tag" href="#menu">MENU</a>
    <a class="nav-tag" href="#contact">CONTACT</a>
  </nav>

  <svg class="book" width="1200" height="1010" viewBox="0 0 1200 1010">
    <defs>
      <linearGradient id="photoFill" x1="0" y1="0" x2="1" y2="1">
        <stop offset="0" stop-color="#3a5560"/>
        <stop offset=".45" stop-color="#b8753a"/>
        <stop offset=".7" stop-color="#e6a860"/>
        <stop offset="1" stop-color="#3a2418"/>
      </linearGradient>
    </defs>
    <path d="M60 400 Q330 440 600 392 L600 998 Q330 975 60 1000 Q72 700 60 400 Z" fill="url(#photoFill)" stroke="var(--page-rim)" stroke-width="5" role="img" aria-label="Photograph of glowing crystal candle holders on a wrought iron stand"/>
    <path d="M613 392 Q880 435 1142 390 Q1162 700 1142 997 Q880 960 613 998 Z" fill="var(--page-dark)" stroke="var(--page-rim)" stroke-width="5"/>
    <g stroke="#9a7a52" stroke-width="3" fill="none">
      <path d="M580 452 h40"/><path d="M580 500 h40"/><path d="M580 548 h40"/>
      <path d="M580 596 h40"/><path d="M580 644 h40"/><path d="M580 692 h40"/>
      <path d="M580 740 h40"/><path d="M580 788 h40"/><path d="M580 836 h40"/>
      <path d="M580 884 h40"/><path d="M580 932 h40"/>
    </g>
    <g fill="#0a0a0a">
      <circle cx="582" cy="452" r="5"/><circle cx="582" cy="500" r="5"/><circle cx="582" cy="548" r="5"/>
      <circle cx="582" cy="596" r="5"/><circle cx="582" cy="644" r="5"/><circle cx="582" cy="692" r="5"/>
      <circle cx="582" cy="740" r="5"/><circle cx="582" cy="788" r="5"/><circle cx="582" cy="836" r="5"/>
      <circle cx="582" cy="884" r="5"/><circle cx="582" cy="932" r="5"/>
    </g>
    <g fill="none" stroke="#a0523a" stroke-width="2">
      <path d="M674 843 L666 862 L674 881"/>
      <path d="M1110 843 L1118 862 L1110 881"/>
    </g>
  </svg>

  <section class="page-content">
    <h1 class="section-title">Welcome to <span class="accent">Villa Rosmar</span></h1>
    <div class="title-rule"></div>
    <p class="intro-text">Lorem ipsum dolor sit amet, consectetur adipiscing elit. Nullam ultricies commodo semper. In volutpat, risus a pretium fringilla, mauris elit tempus eros, non porta lorem ipsum non tortor. Sed dapibus adipiscing massa, ac dictum nunc tempus sed. Nulla facilisi. Fusce blandit sapien non risus blandit laoreet varius nec nisi. Vestibulum ante ipsum primis in faucibus orci luctus et ultrices posuere cubilia Curae; Maecenas laoreet lorem vel ipsum malesuada vel iaculis ante iaculis. Morbi vitae nisi quis dui gravida faucibus.</p>
    <h2 class="category-title">Category</h2>
  </section>

  <article class="category-item">
    <div class="item-photo" role="img" aria-label="Photograph of a chocolate dessert with ice cream on a white plate"></div>
    <h3 class="item-title">Chocolates</h3>
    <p class="item-text">Lorem ipsum dolor sit amet, consectetur adipiscing elit. Nullam ultricies commodo semper.</p>
    <p class="item-more">Loremipadcing Lorem...</p>
  </article>

  <footer class="site-footer">
    <nav class="footer-links">
      <a href="#home">Home</a><span class="sep">|</span>
      <a href="#about">About</a><span class="sep">|</span>
      <a href="#menu">Menu</a><span class="sep">|</span>
      <a href="#terms">Terms</a><span class="sep">|</span>
      <a href="#contact">Contact us</a>
    </nav>
    <p class="copyright"><span>All Rights Reserved@VillaRosmar</span></p>
    <a class="social-link" href="#friendbook">
      <span class="visit">VISIT US ON</span>
      <span class="network">Friendbook</span>
    </a>
  </footer>

</div>
</body>
</html>
```